Webdesign für Reittherapeutin
Zielgruppe
Ich bin Reittherapeutin und biete auf unserem privaten Hof Reittherapie für Kinder, Jugendliche und Erwachsene an. Die Therapieeinheiten finden im Freien statt, also auf dem Sandplatz oder im Gelände. In der Reittherapie steht nicht das Reiten, sonden der Umgang und die Beziehung zum Pferd im Vordergrund.
Aufgabenstellung
Mir gefallen Designs in Naturtönen, welche auch gut zu meiner Tätigkeit passen. Ich habe bereits ein Logo, einen Namen (Wiesen erleben) und die Domaine (www.wiesen-erleben.ch) ebenso.

```html
<!DOCTYPE html>
<html lang="de">
<head>
<meta charset="utf-8">
<title>Wiesen erleben – Reittherapie</title>
<link rel="stylesheet" href="https://fonts.googleapis.com/css2?family=Fira+Sans:wght@300;400;500&family=Fira+Sans+Condensed:wght@300;400;500&display=swap">
<style>
:root{
  --sidebar:#bcc36f;
  --accent:#b0ba5c;
  --nav-text:#6d6a48;
  --light:#eeebec;
  --grey:#787777;
  --ink:#1e1e1e;
  --white:#ffffff;
  --black:#000000;
  --map:#dddad5;
}
*{margin:0;padding:0;box-sizing:border-box}
html,body{width:1200px;height:817px;overflow:hidden;background:var(--white)}
body{position:relative;font-family:"Fira Sans",sans-serif;color:var(--ink)}
.page{position:absolute;top:0;width:595px}
.page--home{left:0;height:813px}
.page--about{left:605px;height:663px}

.sidebar{position:absolute;left:0;top:0;width:101px;height:100%;background:var(--sidebar)}
.brand{position:absolute;left:0;top:0;width:101px;height:88px;background:var(--white);display:flex;flex-direction:column;align-items:center;justify-content:center;gap:6px}
.brand-dot{width:30px;height:30px;border-radius:50%;background:#2b9aa0}
.brand-name{font-family:"Fira Sans",sans-serif;font-weight:400;font-size:10px;color:#2b9aa0;white-space:nowrap}
.nav{position:absolute;top:119px;left:0;width:101px;list-style:none;text-align:center}
.nav li{font-family:"Fira Sans Condensed",sans-serif;font-size:10.5px;color:var(--nav-text);height:26.7px}

.hero{position:absolute;left:101px;top:0;width:494px;height:179px;background:linear-gradient(180deg,#6d9fd6 0%,#a9c4e2 36%,#8d8068 48%,#4a3a2c 70%,#2a2420 100%)}
.hero-title{position:absolute;left:274px;top:121px;font-family:"Fira Sans",sans-serif;font-weight:400;font-size:35px;line-height:40px;letter-spacing:.5px;color:var(--white)}
.hero-rule{position:absolute;left:276px;top:162px;width:140px;height:1px;background:var(--accent)}
.hero-sub{position:absolute;left:276px;top:164px;font-family:"Fira Sans Condensed",sans-serif;font-weight:300;font-size:7.4px;color:#f1f1f1;letter-spacing:.2px}

.intro{position:absolute;left:101px;top:179px;width:494px;height:178px;background:var(--light)}
.intro-text{position:absolute;left:36px;top:37px;width:194px;font-size:6.3px;line-height:6.1px;text-align:justify;hyphens:auto}
.intro-text p{margin-bottom:6.5px}
.intro-list{position:absolute;left:36px;top:37px;list-style:none;font-size:6.3px}
.intro-list li{height:12.7px}
.intro-photo{position:absolute;left:257px;top:18px;width:210px;height:139px}
.photo--session{background:linear-gradient(180deg,#78a6db 0%,#b7cde6 45%,#6f6a58 60%,#2c2a2c 100%)}
.photo--ponies{background:linear-gradient(180deg,#9aa3a4 0%,#7d7a6c 35%,#6f8a55 55%,#8a8784 100%)}

.info{position:absolute;left:101px;top:357px;width:494px;background:var(--grey);color:var(--white)}
.info--home{height:322px}
.info--about{height:180px}
.section-title{position:absolute;font-family:"Fira Sans",sans-serif;font-weight:400;font-size:11px;line-height:13px;letter-spacing:.3px}
.section-rule{position:absolute;width:36px;height:1px;background:var(--accent)}
.col{position:absolute;top:40px;width:104px;font-family:"Fira Sans Condensed",sans-serif;font-size:6.1px;line-height:6.35px;text-align:justify;hyphens:auto}
.col p+p{margin-top:6.35px}
.lead{position:absolute;font-family:"Fira Sans Condensed",sans-serif;font-weight:300;font-size:7px;line-height:10.2px}
.bullets{position:absolute;list-style:none;font-family:"Fira Sans Condensed",sans-serif;font-size:6.2px;line-height:6.35px}

.contact{position:absolute;left:101px;width:494px;background:var(--light)}
.contact--home{top:679px;height:103px}
.contact--about{top:537px;height:99px}
.contact-photo{position:absolute;left:29px;width:58px;height:65px;background:linear-gradient(180deg,#8fb0cf 0%,#7e7566 45%,#2b3346 100%)}
.contact-role{position:absolute;left:133px;font-family:"Fira Sans Condensed",sans-serif;font-size:9.5px;line-height:11px;color:var(--accent)}
.contact-phone{position:absolute;left:133px;font-family:"Fira Sans Condensed",sans-serif;font-size:9.5px;line-height:11px;color:var(--ink)}
.contact-address{position:absolute;left:133px;font-size:6.3px;line-height:6.4px;font-style:normal}
.contact-mail{position:absolute;left:133px;font-size:6.5px;line-height:8px}
.contact-button{position:absolute;left:133px;width:54px;height:13px;border:1px solid var(--accent);font-family:"Fira Sans Condensed",sans-serif;font-size:3.8px;color:var(--accent);display:flex;align-items:center;padding-left:3px;letter-spacing:.2px}
.contact-map{position:absolute;left:274px;width:114px;height:75px;background:var(--map)}

.footer{position:absolute;left:101px;width:494px;background:var(--black);color:var(--white);text-align:center;font-family:"Fira Sans Condensed",sans-serif;font-size:4px;letter-spacing:.1px}
.footer--home{top:782px;height:31px;padding-top:10px}
.footer--about{top:636px;height:27px;padding-top:9px}
.footer p{line-height:8.5px}
</style>
</head>
<body>

<section class="page page--home">
  <aside class="sidebar">
    <div class="brand"><span class="brand-dot"></span><span class="brand-name">Wiesen erleben</span></div>
    <ul class="nav"><li>Reittherapie</li><li>Angebot</li><li>Über mich</li><li>Pferde</li><li>Kontakt</li></ul>
  </aside>

  <header class="hero" role="img" aria-label="Foto: Reiterin liegt entspannt auf einem schwarzen Pony, dahinter Felder und blauer Himmel">
    <h1 class="hero-title">Reittherapie</h1>
    <span class="hero-rule"></span>
    <p class="hero-sub">Beziehung zwischen Mensch und Pferd</p>
  </header>

  <section class="intro">
    <div class="intro-text">
      <p>Für alle Kinder, Jugendliche und Erwachsene geeignet, welche einen liebevollen und angstfreien Umgang mit dem Pferd suchen.</p>
      <p>Förderung der körperlichen, geistigen, emotionalen und sozialen Entwicklung mit oder auf dem Pferd.</p>
      <p>Förderung der Sinne und Wahrnehmung.</p>
      <p>Umgang und Pflege des Pferdes erlernen</p>
      <p>Sitzen, reiten und entspannen auf dem Pferd.</p>
    </div>
    <div class="intro-photo photo--session" role="img" aria-label="Foto: Therapeutin reicht einer Reiterin auf dem Pony eine grüne Schale"></div>
  </section>

  <section class="info info--home">
    <h2 class="section-title" style="left:35px;top:12px">Was ist Reittherapie?</h2>
    <span class="section-rule" style="left:35px;top:29px"></span>
    <div class="col" style="left:58px">Die Reittherapie ist eine ganzheitliche und individuelle Förderung mit und auf dem Pferd. Das heisst, der Umgang mit dem Pferd fördert sämtliche Bereiche der körperlichen, geistigen, emotionalen und sozialen Entwicklung. Es kann explizit auf gewünschte oder erstrebenswerte Förderziele eingegangen werden und diese je nach Bedarf angepasst und verändert werden. Es steht nicht das Erlernen des Reitens im Vordergrund, sondern vielmehr der Kontakt und die Beziehung zwischen dem Menschen und dem Pferd.</div>
    <div class="col" style="left:195px">Die Reittherapie beginnt schon am Boden, das Pflegen und Vorbereiten des Pferdes gehört genauso zur therapeutischen Behandlung, wie das Sitzen, Reiten und Entspannen auf dem Pferd. Die Arbeit am Boden ist ein wichtiger Bestandteil der Reittherapie, sie fördert vor allem die Wahrnehmung und die sozialen Fähigkeiten und ist Voraussetzung für den Beziehungsaufbau zwischen Pferd und Mensch. Der respektvolle und vertraute Umgang miteinander ist wichtig, damit der Klient auf dem Pferd loslassen und sich auf die verschiedenen Übungen mit dem Pferd einlassen kann.</div>
    <div class="col" style="left:341px">
      <p>Das therapeutische Reiten eignet sich grundsätzlich für alle Kinder und Erwachsene, die einen liebevollen, angstfreien Umgang mit dem Pferd suchen und zu einem sanften Weg zum Reiten bereit sind.</p>
      <p>Für die Förderung der verschiedensten Bereiche, für Rituale oder zur Abwechslung im Reittherapiealltag, werden gerne unterschiedliche Materialien, wie zum Beispiel verschieden farbige Tücher, Bälle in diversen Grössen, Würfel, Spiele, Fingerfarben oder Tastsäckchen, eingesetzt. Der Fantasie sind keine Grenzen gesetzt, solange die Sicherheit von Klienten und Pferd gewährleistet sind.</p>
    </div>

    <h2 class="section-title" style="left:35px;top:182px">Anwendungsgebiet und Wirkung</h2>
    <span class="section-rule" style="left:35px;top:199px"></span>
    <span class="section-rule" style="left:246px;top:199px"></span>
    <p class="lead" style="left:35px;top:204px">Besonders hilfreich ist die Reittherapie<br>für Kinder, Jugendliche und Erwachsene<br>aller Altersstufen zur Förderung:</p>
    <p class="lead" style="left:246px;top:204px">Häufige Anwendungsgebiete sind:</p>
    <ul class="bullets" style="left:35px;top:247px">
      <li>– von Entwicklungsverzögerungen</li>
      <li>– von Verhaltensauffälligkeiten</li>
      <li>– der Aufmerksamkeit, Konzentration und Selbständigkeit</li>
      <li>– des Selbstbewusstseins und Umgang mit Emotionen</li>
      <li>– sozialer Kompetenzen</li>
      <li>– der Lernmotivation</li>
      <li>– der Wahrnehmung, Koordination und Körperbewusstseins</li>
      <li>– der Sprachentwicklung</li>
      <li>– intensiver Natur- und Tiererfahrungen</li>
      <li>– der seelischen Ausgeglichenheit und Stabilisierung</li>
    </ul>
    <ul class="bullets" style="left:246px;top:247px">
      <li>– Wahrnehmungsstörungen, Konzentrationsstörungen ADS / ADHS</li>
      <li>– Lernschwierigkeiten</li>
      <li>– Stress, Burnout</li>
      <li>– Essstörungen</li>
      <li>– Depressionen</li>
      <li>– Körperliche und geistige Behinderung</li>
    </ul>
  </section>

  <section class="contact contact--home">
    <div class="contact-photo" style="top:25px" role="img" aria-label="Foto: Reittherapeutin mit Pferd"></div>
    <p class="contact-role" style="top:10px">Reittherapeutin</p>
    <p class="contact-phone" style="top:24px">0041 79 000 12 34</p>
    <address class="contact-address" style="top:42px">Lena Brunner<br>Mattenweg 4<br>8400 Wiesdorf</address>
    <p class="contact-mail" style="top:64px">info@wiesen-erleben.ch</p>
    <span class="contact-button" style="top:78px">&gt;&nbsp; KONTAKT AUFNEHMEN</span>
    <div class="contact-map" style="top:12px" role="img" aria-label="Karte: Lage des Hofes"></div>
  </section>

  <footer class="footer footer--home">
    <p>ZAHLUNGSBEDINGUNGEN</p>
    <p>IMPRESSUM &nbsp;DATENSCHUTZ &nbsp;SITEMAP</p>
  </footer>
</section>

<section class="page page--about">
  <aside class="sidebar">
    <div class="brand"><span class="brand-dot"></span><span class="brand-name">Wiesen erleben</span></div>
    <ul class="nav"><li>Reittherapie</li><li>Angebot</li><li>Über mich</li><li>Pferde</li><li>Kontakt</li></ul>
  </aside>

  <header class="hero" role="img" aria-label="Foto: Reiterin liegt entspannt auf einem schwarzen Pony, dahinter Felder und blauer Himmel">
    <h1 class="hero-title">Reittherapie</h1>
    <span class="hero-rule"></span>
    <p class="hero-sub">Beziehung zwischen Mensch und Pferd</p>
  </header>

  <section class="intro">
    <ul class="intro-list">
      <li>Lena Brunner</li>
      <li>Seit 2019 zertifizierte Reittherapeutin bei Therapiepferde-Netz</li>
      <li>Familienfrau und Pferdewirtin</li>
      <li>Finanzfrau in einer sozialen Institution</li>
    </ul>
    <div class="intro-photo photo--ponies" role="img" aria-label="Foto: Zwei Ponys auf dem Hofplatz, eines geritten"></div>
  </section>

  <section class="info info--about">
    <h2 class="section-title" style="left:34px;top:12px">Über mich</h2>
    <span class="section-rule" style="left:34px;top:29px"></span>
    <h2 class="section-title" style="left:326px;top:12px">Meine Pferde</h2>
    <span class="section-rule" style="left:326px;top:29px"></span>
    <div class="col" style="left:58px">Im 2019 durfte ich die Ausbildung zur Reittherapeutin erfolgreich abschliessen und meinen Traum, zusammen mit meinen Pferden anderen Menschen etwas Gutes zu tun, wahr werden lassen. Mein grosser Wunsch ist es, Kindern, Jugendlichen und auch Erwachsenen, die bereit sind, sich in entspannter Atmosphäre dem Pferd zu nähern, das Wesen Pferd und seine wunderbaren Eigenschaften näher zu bringen. Dabei sollen die Freude, der Spass und die Beziehung zum Pferd im Vordergrund stehen.</div>
    <div class="col" style="left:194px">Die Pferde und ihre Faszination begleiten mich seit meiner Kindheit und begeistern und erfreuen mich bis heute. Ich habe das grosse Glück, mit meiner Familie und den Pferden mitten im Naherholungsgebiet des Wiesdorferfeldes zu Hause zu sein. Unmittelbar angrenzend an unser Grundstück liegt das grösste Auengebiet des Schweizer Mittellandes. Dieses bietet eine wunderbare Natur, Erholung und Ruhe.</div>
    <div class="col" style="left:341px">
      <p>Das therapeutische Reiten eignet sich grundsätzlich für alle Kinder und Erwachsene, die einen liebevollen, angstfreien Umgang mit dem Pferd suchen und zu einem sanften Weg zum Reiten bereit sind.</p>
      <p>Für die Förderung der verschiedensten Bereiche, für Rituale oder zur Abwechslung im Reittherapiealltag, werden gerne unterschiedliche Materialien, wie zum Beispiel verschieden farbige Tücher, Bälle in diversen Grössen, Würfel, Spiele, Fingerfarben oder Tastsäckchen, eingesetzt. Der Fantasie sind keine Grenzen gesetzt, solange die Sicherheit von Klienten und Pferd gewährleistet sind.</p>
    </div>
  </section>

  <section class="contact contact--about">
    <div class="contact-photo" style="top:22px" role="img" aria-label="Foto: Reittherapeutin mit Pferd"></div>
    <p class="contact-role" style="top:6px">Reittherapeutin</p>
    <p class="contact-phone" style="top:20px">0041 79 000 12 34</p>
    <address class="contact-address" style="top:37px">Lena Brunner<br>Mattenweg 4<br>8400 Wiesdorf</address>
    <p class="contact-mail" style="top:59px">info@wiesen-erleben.ch</p>
    <span class="contact-button" style="top:74px">&gt;&nbsp; KONTAKT AUFNEHMEN</span>
    <div class="contact-map" style="top:8px" role="img" aria-label="Karte: Lage des Hofes"></div>
  </section>

  <footer class="footer footer--about">
    <p>ZAHLUNGSBEDINGUNGEN</p>
    <p>IMPRESSUM &nbsp;DATENSCHUTZ &nbsp;SITEMAP</p>
  </footer>
</section>

</body>
</html>
```